Tamsin Vale Chiropractic Web Design

We need a fully operating Web site design INCLUDING the code for a Chiropractic Clinic based in Auckland New Zealand to target people from different financial backgrounds.

We need 4 Pages as followed:
1. Home: includes Slideshow of the clinic, General information about chiropractic, option for "Request an appointment", and it would be nice to have a picture on the top right side of the header and the clinic's name and logo on the top left side. on the bottom right we would like a small section for "Testimonial" (A good example: http://www.brindlemoorstudios.example/ )
(A good example for slide show is: http://www.pelvoro.example.nz/)
(A good example for the header is: http://www.spinehavenwelt.example.com/)

2. About Us: this section will include the background information of the company, and a section for our staff (which will includes a photo and description of each person/staff which can be changedanytime)
(a good example: http://www.fernwaybackcare.example.nz/)

3. Contact: includes location, map, contact numbers, email, and a contact box (A good example: http://www.brindlemoorstudios.example/contact/)

4. Services: includes our products, adjustment equipment, chiropractic products for sale, few pictures of patients while under chiropractic care/adjustment tables

We would also like to add "social networking" options on the bottom left side of every page (Facebook, twitter, Blog, Google+)

Please check the following links to get a feel of our favorite designs:
http://www.spinehavenwelt.example.com/
http://www.fernwaybackcare.example.nz/
http://www.pelvoro.example.nz/
http://www.dunmerespinalcentre.example.com/
http://www.quietbirch.example.nz/
http://www.pwo.example.nz/index-1.html
http://home.corelinespine.example.nz/home/

we would like to have full access to the back-end- admin of the website to be able to change and add any pictures or texts.
Updates

Hi Lovely Designer,

thank you so much for your proposed designs. We just uploaded the original source file of our logo, for you all to have access on it to facilitate your work. 

Enjoy your day

Leni

Target Market(s)

People with different financial background as well as we are located in the artistic part of town, so appealing to those crowd is important to us.

Industry/Entity Type

Financial

Requirements
Must have
• 1.color similar to the logo or darker colors (Dark and rich colors are prefered)
2. more artistic than a basic doctors' clinic
3. I would like the opening of the web to bring art, tranquility and peaceful images into mind
Should not have
• Not bombarded with lots of info and pics in one page, not too busy and crowded

```html
<!DOCTYPE html>
<html lang="en">
<head>
<meta charset="utf-8">
<title>Tamsin Vale Chiropractic</title>
<link href="https://fonts.googleapis.com/css2?family=Ubuntu:wght@400;500;700&family=Open+Sans:ital,wght@0,400;0,700;1,700&display=swap" rel="stylesheet">
<style>
:root{
  --navy:#0a3f7c;
  --navy-deep:#062e61;
  --navy-light:#1a5fa6;
  --lime:#8cc63f;
  --lime-dark:#5aa51b;
  --paper:#e9e9e9;
  --ink:#2b2b2b;
  --heading-blue:#0b5aa3;
  --footer:#1e1e1e;
  --footer-text:#c9c9c9;
  --star:#f26b11;
}
*{margin:0;padding:0;box-sizing:border-box}
html,body{width:904px;height:1200px;overflow:hidden}
body{background:var(--paper);font-family:"Open Sans",Arial,sans-serif;color:var(--ink);position:relative}
.site-header{position:absolute;left:0;top:0;width:904px;height:552px;
  background:radial-gradient(ellipse at 80% 20%,#1b5fa6 0%,var(--navy) 45%,var(--navy-deep) 100%)}
.brand{position:absolute;left:48px;top:30px;display:flex;align-items:center;gap:10px;
  font-family:"Ubuntu",sans-serif;font-weight:400;font-size:28px;color:var(--lime);letter-spacing:.5px;line-height:1.05}
.brand-mark{width:16px;height:16px;border-radius:50%;background:var(--lime);flex:none}
.phone{position:absolute;right:72px;top:44px;display:flex;align-items:center;gap:8px;
  font-family:"Ubuntu",sans-serif;font-weight:700;font-size:22px;color:#fff}
.main-nav{position:absolute;left:165px;top:127px;display:flex;font-family:"Ubuntu",sans-serif;font-size:16px}
.main-nav a{color:#fff;text-decoration:none;height:38px;line-height:38px;padding:0 24px;margin-right:10px}
.main-nav a.active{background:linear-gradient(#9bd34a,var(--lime-dark));padding:0 24px 0 30px}
.slider{position:absolute;left:56px;top:187px;width:791px;height:325px;background:#fff;padding:6px;
  box-shadow:0 10px 18px rgba(0,0,0,.35)}
.slider-photo{width:100%;height:100%;background:linear-gradient(180deg,#9a8a3c 0%,#6f7a35 35%,#a07a4a 70%,#8a5a38 100%)}
.content-divider{position:absolute;left:0;top:552px;width:904px;height:5px;background:#fff}
.intro-logo{position:absolute;left:62px;top:582px;display:flex;align-items:center;gap:10px;
  font-family:"Ubuntu",sans-serif;font-size:24px;color:#555;line-height:1.05}
.intro-logo .brand-mark{background:#666;width:14px;height:14px}
.cta{position:absolute;left:617px;top:568px;width:223px;height:66px;border-radius:6px;border:2px solid #fff;
  background:linear-gradient(#a8dc4e,#6cb423);box-shadow:0 2px 5px rgba(0,0,0,.3);text-decoration:none;
  font-family:"Ubuntu",sans-serif;color:#fff;padding:10px 0 0 18px}
.cta small{display:block;font-size:13px;font-weight:400}
.cta strong{display:block;font-size:20px;font-weight:700;color:#fff200;line-height:1.1}
.cta svg{position:absolute;right:2px;top:2px}
.rule{position:absolute;left:92px;top:643px;width:756px;border-top:1px dotted #aaa}
.intro-photo{position:absolute;left:66px;top:653px;width:171px;height:152px;background:#fff;padding:6px;box-shadow:0 1px 3px rgba(0,0,0,.25)}
.intro-photo div{width:100%;height:100%;background:linear-gradient(135deg,#3fb6d9,#1a86b0 50%,#b57a5a)}
.intro-text{position:absolute;left:265px;top:658px;width:583px;font-size:10.5px;line-height:16.5px;text-align:justify}
.intro-text p+p{margin-top:16px}
.intro-text em{font-weight:700}
.col{position:absolute;top:852px}
.col h2{font-family:"Ubuntu",sans-serif;font-weight:500;font-size:15px;color:var(--heading-blue);
  padding-left:14px;border-left:2px solid var(--lime);line-height:18px;margin-left:12px}
.col-card{width:230px;height:100px;background:#fff;padding:6px;box-shadow:0 1px 3px rgba(0,0,0,.25);margin-top:24px}
.col-card div{width:100%;height:100%}
.col p{font-family:Arial,sans-serif;font-size:11px;line-height:16.5px;width:218px;margin:12px 0 0 6px;text-align:justify}
.col-1{left:66px}
.col-2{left:346px}
.col-3{left:613px}
.vline{position:absolute;top:880px;height:215px;border-left:1px solid #d2d2d2}
.review{margin:14px 0 0 23px;width:210px}
.review h3{font-family:"Ubuntu",sans-serif;font-weight:500;font-size:13px;color:#222}
.stars{color:var(--star);font-size:13px;letter-spacing:1px;margin-top:4px}
.review .meta{font-family:Arial,sans-serif;font-style:italic;font-size:8.5px;color:var(--heading-blue);margin-top:2px}
.review .body{font-family:Arial,sans-serif;font-size:9.5px;line-height:15px;margin:2px 0 0;width:210px;text-align:left}
.review+.review{border-top:1px dotted #bbb;padding-top:10px;margin-top:8px}
.site-footer{position:absolute;left:0;top:1117px;width:904px;height:83px;background:var(--footer);border-top:6px solid #3a3a3a;
  font-family:Arial,sans-serif;color:var(--footer-text)}
.social{position:absolute;left:46px;top:8px}
.social h4,.contact h4{font-family:"Ubuntu",sans-serif;font-weight:500;font-size:13px;color:#ccc}
.social ul{list-style:none;display:flex;gap:6px;margin-top:8px}
.social li{width:27px;height:27px;border-radius:50%;border:2px solid #ddd}
.social li:nth-child(1){background:#3b5a9a}.social li:nth-child(2){background:#3aa5d8}
.social li:nth-child(3){background:#cfcfcf}.social li:nth-child(4){background:#f26b11}.social li:nth-child(5){background:#9a9a9a}
.fsep{position:absolute;top:12px;height:60px;border-left:1px dotted #555}
.foot-nav{position:absolute;left:250px;top:18px;width:376px;text-align:center;font-size:10.5px;line-height:20px}
.contact{position:absolute;left:668px;top:12px}
.contact a{display:block;font-family:"Ubuntu",sans-serif;font-weight:500;font-size:13px;color:#fff;text-decoration:none;margin-top:5px}
</style>
</head>
<body>
<header class="site-header">
  <div class="brand"><span class="brand-mark"></span><span>Tamsin Vale<br>Chiropractic</span></div>
  <div class="phone">
    <svg width="32" height="32" viewBox="0 0 32 32"><circle cx="16" cy="16" r="14" fill="none" stroke="#fff" stroke-width="2.5"/><path d="M11 9c-2 1-2 4 0 8s5 7 8 7c2 0 3-1 3-2l-3-3-2 1c-1-1-3-3-4-5l1-2-3-4z" fill="#fff"/></svg>
    <span>(123) 456 7801</span>
  </div>
  <nav class="main-nav">
    <a class="active" href="#">Home</a><a href="#">About Us</a><a href="#">Services</a><a href="#">Testimonials</a><a href="#">Contact Us</a>
  </nav>
  <div class="slider"><div class="slider-photo" role="img" aria-label="Family riding bicycles along an autumn forest path"></div></div>
</header>
<div class="content-divider"></div>

<div class="intro-logo"><span class="brand-mark"></span><span>Tamsin Vale<br>Chiropractic</span></div>
<a class="cta" href="#"><small>Click Here to Make an</small><strong>APPOINTMENT</strong>
  <svg width="58" height="58" viewBox="0 0 58 58"><circle cx="29" cy="29" r="26" fill="#f4f4f4" stroke="#9a9a9a" stroke-width="3"/><line x1="29" y1="29" x2="29" y2="12" stroke="#222" stroke-width="2"/><line x1="29" y1="29" x2="42" y2="38" stroke="#1a3fa0" stroke-width="2"/></svg>
</a>
<div class="rule"></div>

<div class="intro-photo"><div role="img" aria-label="Illustration of a person's back with the spine highlighted"></div></div>
<div class="intro-text">
  <p><em>Lorem ipsum dolor sit amet, consectetuer adipiscing elit. Nam cursus. Morbi ut mi. Nullam enim leo, egestas</em> id, condimentum at, laoreet mattis, massa. Sed eleifend nonummy diam. Praesent mauris ante, elementum et, bibendum at, posuere sit amet, nibh. Duis tincidunt lectus quis dui viverra vestibulum. Suspendisse vulputate aliquam dui. Nulla elementum dui ut augue. Aliquam vehicula mi at mauris.</p>
  <p>Morbi magna magna, tincidunt a, mattis non, imperdiet vitae, tellus. Sed odio est, auctor ac, sollicitudin in, consequat vitae, orci. Fusce id felis. Vivamus sollicitudin metus eget eros.</p>
</div>

<section class="col col-1">
  <h2>Personal Chiropractic Care</h2>
  <div class="col-card"><div role="img" aria-label="Hands giving a shoulder adjustment" style="background:linear-gradient(90deg,#7a6a60,#e3c8b4 45%,#cfd3da)"></div></div>
  <p>Pellentesque habitant morbi tristique senectus et netus et malesuada fames ac turpis egestas. In posuere felis nec tortor.</p>
</section>
<div class="vline" style="left:321px"></div>
<section class="col col-2">
  <h2>Corporate Chiropractic</h2>
  <div class="col-card"><div role="img" aria-label="Doctor explaining a spine model to a patient" style="background:linear-gradient(90deg,#8fa4b8,#e8e4df 45%,#4e6e94)"></div></div>
  <p>Pellentesque habitant morbi tristique senectus et netus et malesuada fames ac turpis egestas. In posuere felis nec tortor.</p>
</section>
<div class="vline" style="left:601px"></div>
<section class="col col-3">
  <h2>Recent Testimonials</h2>
  <div class="review">
    <h3>Thanks for the treatment</h3>
    <div class="stars">★★★★★</div>
    <div class="meta">May 12, 2013 by Maren</div>
    <p class="body">Pellentesque habitant morbi tristique senectus et netus...</p>
  </div>
  <div class="review">
    <h3>Ut accumsan ultricies elit</h3>
    <div class="stars">★★★★★</div>
    <div class="meta">May 12, 2013 by Maren</div>
    <p class="body">Pellentesque habitant morbi tristique senectus et netus...</p>
  </div>
</section>

<footer class="site-footer">
  <div class="social">
    <h4>Get Connected</h4>
    <ul aria-label="Social networks"><li></li><li></li><li></li><li></li><li></li></ul>
  </div>
  <div class="fsep" style="left:250px"></div>
  <div class="foot-nav">
    <div>Home &nbsp;|&nbsp; About Us &nbsp;|&nbsp; Services &nbsp;|&nbsp; Testimonials &nbsp;|&nbsp; Contact Us</div>
    <div>TamsinVale Chiropractic , Copy Right © 2013</div>
  </div>
  <div class="fsep" style="left:630px"></div>
  <div class="contact">
    <h4>Contact Us @</h4>
    <a href="#">info@tamsinvalechiro.example</a>
  </div>
</footer>
</body>
</html>
```